Accounting firm needs a postcard design

We need a postcard design for our accounting office for a advertising campaign mailing we do yearly from a mail list we create. We are a full-service accounting office that has been in business for 35 years. I have attached our logo in different formats along with a document with a description of the services we provide. I have also attached my business card and the business card of our CPA. The business cards will have contact information for the postcard design. The contact email that will need to be on the postcard is contact@harlowledgerpartners.com.

```html
<!DOCTYPE html>
<html lang="en">
<head>
<meta charset="utf-8">
<title>Harlow Ledger Partners – Postcard</title>
<link href="https://fonts.googleapis.com/css2?family=Libre+Baskerville:wght@400;700&family=Montserrat:wght@400;500;600;700&family=Arimo:wght@400&display=swap" rel="stylesheet">
<style>
:root{
  --navy:#1b3170;
  --navy-deep:#172a63;
  --blue:#1d6fb5;
  --green:#7ac143;
  --green-dark:#3d9a2c;
  --ink:#1e2b55;
  --text:#222;
  --paper:#ffffff;
  --paper-soft:#f4f5f6;
}
*{margin:0;padding:0;box-sizing:border-box}
html,body{width:1200px;height:2602px;overflow:hidden}
body{background:linear-gradient(180deg,#e4e4e4,#cfcfcf);position:relative;font-family:"Montserrat",sans-serif;color:var(--text)}
.postcard{position:absolute;left:98px;width:993px;height:663px;background:var(--paper);overflow:hidden;box-shadow:0 14px 22px rgba(0,0,0,.35)}
.postcard--front{top:598px;background:linear-gradient(135deg,var(--paper) 0%,var(--paper-soft) 100%)}
.postcard--back{top:1341px}
.shapes{position:absolute;left:0;top:0}
.abs{position:absolute}

.brand-mark{width:64px;height:64px;border-radius:50%;background:var(--navy)}
.brand-name{font-family:"Libre Baskerville",serif;font-weight:700;color:var(--navy);letter-spacing:2px;white-space:nowrap}
.brand-tagline{font-family:"Montserrat",sans-serif;font-size:9px;color:#333;white-space:nowrap}

.intro-bar{width:3px}
.intro-name{font-family:"Libre Baskerville",serif;font-size:21px;line-height:27px;color:var(--ink)}
.intro-name .accent{color:var(--green-dark)}
.intro-copy{font-size:21px;line-height:29px;color:var(--ink)}
.intro-copy strong{font-weight:600}

.what-we-do{font-weight:700;color:#fff;font-size:15px;line-height:17px;text-align:right}
.service-list{list-style:none;color:#fff;font-size:13px;font-weight:500}
.service-list li{height:18px;display:flex;align-items:center;gap:10px}
.service-list li::before{content:"";width:7px;height:7px;border:1px solid #fff}

.contact-call{color:var(--green);font-weight:600;font-size:19px}
.contact-phone{color:#fff;font-weight:600;font-size:28px;display:flex;align-items:center;gap:6px;white-space:nowrap}
.contact-line{font-size:12.5px;line-height:16px;color:#fff;white-space:nowrap}
.contact-line::before{content:"";display:inline-block;width:9px;height:9px;border:1.5px solid currentColor;border-radius:50%;margin-right:5px;vertical-align:-1px}
.contact-line .accent{color:var(--green)}
.contact--back .contact-phone{color:var(--navy)}
.contact--back .contact-line{color:var(--navy)}

.service h3{font-size:17px;font-weight:600;color:var(--green);letter-spacing:.2px}
.service p{font-family:"Arimo",sans-serif;font-size:12.4px;line-height:15.5px;color:#fff;margin-top:3px;width:450px}

.stamp-box{width:112px;height:113px;border:1px solid #333}
.address-line{width:265px;height:1px;background:#333}
</style>
</head>
<body>

<!-- FRONT -->
<section class="postcard postcard--front">
  <svg class="shapes" width="993" height="663" viewBox="0 0 993 663">
    <defs>
      <linearGradient id="band" x1="0" y1="0" x2="1" y2="0">
        <stop offset="0" stop-color="#1a2f6e"/>
        <stop offset="1" stop-color="#1d6fb5"/>
      </linearGradient>
      <linearGradient id="wave" x1="0" y1="0" x2="1" y2="0">
        <stop offset="0" stop-color="#3c9a2c"/>
        <stop offset="1" stop-color="#7ac143"/>
      </linearGradient>
      <radialGradient id="photo" cx=".5" cy=".45" r=".6">
        <stop offset="0" stop-color="#b9d48a"/>
        <stop offset=".6" stop-color="#6f9a3a"/>
        <stop offset="1" stop-color="#3f6a24"/>
      </radialGradient>
    </defs>
    <path d="M0,535 C150,490 330,500 470,455 C560,428 700,420 993,380 L993,663 L0,663 Z" fill="url(#band)"/>
    <path d="M0,520 C140,470 300,470 420,455 C460,450 485,440 492,430 L492,448 C470,470 400,478 300,485 C180,495 80,520 0,548 Z" fill="#fff"/>
    <path d="M0,378 C80,330 200,330 300,360 C380,385 450,380 478,386 C470,410 420,420 340,418 C220,414 100,420 0,450 Z" fill="url(#wave)"/>
    <path d="M0,450 C100,420 220,414 340,418 C420,420 470,410 478,386 L484,398 C475,425 420,432 340,432 C220,430 100,438 0,470 Z" fill="#fff"/>
    <path d="M0,470 C100,438 220,430 340,432 C420,432 475,425 484,405 C486,440 460,462 400,468 C300,478 150,480 0,530 Z" fill="url(#wave)"/>
    <path d="M733,40 Q748,40 760,47 L968,167 Q988,179 988,202 L988,452 Q988,475 968,487 L760,607 Q745,615 733,615 Q720,615 706,607 L498,487 Q478,475 478,452 L478,202 Q478,179 498,167 L706,47 Q718,40 733,40 Z" fill="#fff"/>
    <path d="M733,56 Q745,56 755,62 L958,179 Q973,188 973,206 L973,448 Q973,466 958,475 L755,592 Q745,598 733,598 Q721,598 711,592 L508,475 Q493,466 493,448 L493,206 Q493,188 508,179 L711,62 Q721,56 733,56 Z" fill="var(--navy)"/>
    <circle cx="734" cy="327" r="216" fill="url(#photo)" role="img" aria-label="Photo of a glass jar filled with coins with a young green plant growing from it"/>
  </svg>

  <div class="abs brand-mark" style="left:185px;top:52px"></div>
  <div class="abs brand-name" style="left:0;width:434px;top:140px;font-size:17px;text-align:center">HARLOW LEDGER PARTNERS</div>
  <div class="abs brand-tagline" style="left:0;width:434px;top:162px;text-align:center">Tax Preparation | Bookkeeping | Payroll | Entity Formation</div>

  <div class="abs intro-bar" style="left:60px;top:187px;height:48px;background:var(--green)"></div>
  <div class="abs intro-bar" style="left:60px;top:235px;height:88px;background:var(--navy)"></div>
  <div class="abs intro-name" style="left:83px;top:182px">Marian Harlow, <span class="accent">CPA</span><br><span class="accent">Professional Corporation</span></div>
  <div class="abs intro-copy" style="left:84px;top:240px"><strong>Individualized Business</strong> and<br><strong>Personal Accounting services</strong><br>you can trust.</div>

  <div class="abs what-we-do" style="left:40px;top:582px;width:82px">WHAT<br>WE DO</div>
  <svg class="abs" style="left:130px;top:550px" width="12" height="98"><path d="M11,1 H2 V97 H11" fill="none" stroke="#fff" stroke-width="1"/><path d="M4,43 L9,47 L4,51 Z" fill="var(--green)"/></svg>
  <ul class="abs service-list" style="left:140px;top:553px">
    <li>Personal Income Tax</li><li>Business Tax Returns</li><li>Bookkeeping</li><li>Payroll</li><li>Entity Formation</li>
  </ul>

  <div class="abs contact" style="left:400px;top:550px">
    <div class="contact-call">Call us Today</div>
    <div class="contact-phone"><svg width="22" height="22" viewBox="0 0 24 24"><path d="M6.6 10.8a15 15 0 0 0 6.6 6.6l2.2-2.2a1 1 0 0 1 1-.25 11.4 11.4 0 0 0 3.6.57 1 1 0 0 1 1 1V20a1 1 0 0 1-1 1A17 17 0 0 1 3 4a1 1 0 0 1 1-1h3.5a1 1 0 0 1 1 1c0 1.25.2 2.45.57 3.57a1 1 0 0 1-.25 1z" fill="none" stroke="#fff" stroke-width="2"/></svg>(555) 014-2290</div>
    <div class="contact-line" style="margin-top:3px">www.<span class="accent">harlowledgerpartners</span>.com</div>
    <div class="contact-line">contact@<span class="accent">harlowledgerpartners</span>.com</div>
  </div>
</section>

<!-- BACK -->
<section class="postcard postcard--back">
  <svg class="shapes" width="993" height="663" viewBox="0 0 993 663">
    <path d="M0,0 L305,0 L20,165 L20,500 L305,663 L0,663 Z" fill="var(--green)"/>
    <path d="M325,-8 Q340,-8 352,-1 L610,150 Q628,161 628,182 L628,482 Q628,503 610,514 L352,664 Q340,671 325,671 Q310,671 298,664 L40,514 Q22,503 22,482 L22,182 Q22,161 40,150 L298,-1 Q310,-8 325,-8 Z" fill="#fff"/>
    <path d="M325,8 Q337,8 347,14 L598,160 Q612,168 612,185 L612,478 Q612,495 598,503 L347,649 Q337,655 325,655 Q313,655 303,649 L52,503 Q38,495 38,478 L38,185 Q38,168 52,160 L303,14 Q313,8 325,8 Z" fill="var(--navy-deep)"/>
    <g fill="var(--green)" stroke="#fff" stroke-width="3">
      <path d="M95,158 L116,170 L116,193 L95,205 L74,193 L74,170 Z"/>
      <path d="M95,242 L116,254 L116,277 L95,289 L74,277 L74,254 Z"/>
      <path d="M95,347 L116,359 L116,382 L95,394 L74,382 L74,359 Z"/>
      <path d="M95,435 L116,447 L116,470 L95,482 L74,470 L74,447 Z"/>
    </g>
    <g fill="none" stroke="#fff" stroke-width="1.6">
      <rect x="88" y="171" width="14" height="18" rx="1"/><path d="M91,177 H99 M91,181 H99 M91,185 H96"/>
      <rect x="88" y="256" width="14" height="18" rx="1"/><path d="M91,262 H99 M91,266 H99 M91,270 H99"/>
      <circle cx="95" cy="371" r="7"/><path d="M95,364 V371 H102"/>
      <path d="M87,467 V458 M93,467 V453 M99,467 V456 M105,467 V450"/>
    </g>
  </svg>

  <article class="abs service" style="left:133px;top:154px">
    <h3>TAX PREPARATION</h3>
    <p>With over 35 years of experience filing tax returns, we are experts in tax preparation. Including Personal Returns, Corporations, LLC’s, Partnerships and State Franchise Tax Returns</p>
  </article>
  <article class="abs service" style="left:133px;top:239px">
    <h3>BOOKKEEPING</h3>
    <p>Let us take over the day-to-day bookkeeping so you can get back to running your business. We offer assistance with accounting software setup and provide ongoing bookkeeping services. Including frequent journal entries, accounts payables &amp; receivables, sales tax reporting &amp; payments, account reconciliation, and more.</p>
  </article>
  <article class="abs service" style="left:133px;top:342px">
    <h3>FINANCIAL REPORTING</h3>
    <p>We’ll provide easy to understand financial reports that allow you and your team to manage cash flow, create budgets and make forecasting decisions. Depending on your needs, we can provide monthly, quarterly or yearly financial statements.</p>
  </article>
  <article class="abs service" style="left:133px;top:431px">
    <h3>PAYROLL PROCESSING</h3>
    <p>Whether you have 5 employees or 100+, payroll can be an overwhelming and time consuming task. We offer full-service payroll processing. Including employee on boarding, printed or direct deposit checks, quarterly payroll report filing, yearly W-2/W-3 and 1099 printing and filing, and more.</p>
  </article>

  <div class="abs brand-mark" style="left:694px;top:56px;width:52px;height:52px"></div>
  <div class="abs brand-name" style="left:600px;width:240px;top:129px;font-size:13px;letter-spacing:1.5px;text-align:center">HARLOW LEDGER PARTNERS</div>
  <div class="abs brand-tagline" style="left:600px;width:240px;top:146px;font-size:7px;text-align:center">Tax Preparation | Bookkeeping | Payroll | Entity Formation</div>

  <div class="abs stamp-box" style="left:845px;top:40px"></div>
  <div class="abs address-line" style="left:692px;top:328px"></div>
  <div class="abs address-line" style="left:692px;top:387px"></div>
  <div class="abs address-line" style="left:692px;top:445px"></div>

  <div class="abs contact contact--back" style="left:540px;top:542px">
    <div class="contact-call">Call us Today</div>
    <div class="contact-phone"><svg width="22" height="22" viewBox="0 0 24 24"><path d="M6.6 10.8a15 15 0 0 0 6.6 6.6l2.2-2.2a1 1 0 0 1 1-.25 11.4 11.4 0 0 0 3.6.57 1 1 0 0 1 1 1V20a1 1 0 0 1-1 1A17 17 0 0 1 3 4a1 1 0 0 1 1-1h3.5a1 1 0 0 1 1 1c0 1.25.2 2.45.57 3.57a1 1 0 0 1-.25 1z" fill="none" stroke="var(--navy)" stroke-width="2"/></svg>(555) 014-2290</div>
    <div class="contact-line" style="margin-top:3px">www.<span class="accent">harlowledgerpartners</span>.com</div>
    <div class="contact-line">contact@<span class="accent">harlowledgerpartners</span>.com</div>
  </div>
</section>

</body>
</html>
```